Tradeshow Banner Design (Qty2, 6'H x 2'W)

Brightline Works is an Electrical, Fire Alarm, and Security Contracting company. For tradeshows, we would like 2 vertical Banners to put behind our booth. Our colors are Red, Grey & Black. I would like the Banners to be informative on what services we provide, with some appealing Graphic Design. (bwk-qtr.com)
Slogan: Safeguarding Communities Electrical, Fire & Security Solutions
Target Market(s)
Commercial Construction Clients
Industry/Entity Type
Electrical / Construction
Font styles to use
Other font styles liked:
- Aileron
Colors
EB3D1F
EC4F4E
F09395
F8D3D4
FCEDEE
Requirements
Must have
- Our Logo, Color Scheme, Brief Caption of the services we provide
Nice to have
- Appealing Imagery & a modern/simplistic design

```html
<!DOCTYPE html>
<html lang="en">
<head>
<meta charset="utf-8">
<title>Brightline Works – Tradeshow Banners</title>
<link href="https://fonts.googleapis.com/css2?family=Poppins:wght@400;600;700;800&display=swap" rel="stylesheet">
<style>
  :root {
    --stage: #4a4a4c;
    --banner-bg: #dfe3e2;
    --red: #e93537;
    --red-deep: #c72f38;
    --red-tint: rgba(233, 53, 55, 0.92);
    --charcoal: rgba(58, 57, 59, 0.96);
    --ink: #333333;
    --logo-grey: #6b6c6e;
    --white: #ffffff;
  }
  * { box-sizing: border-box; margin: 0; padding: 0; }
  html, body { width: 1200px; height: 1200px; overflow: hidden; }
  body { background: var(--stage); font-family: 'Poppins', sans-serif; position: relative; }

  .banner { position: absolute; top: 104px; width: 331px; height: 992px; background: var(--banner-bg); overflow: hidden; }
  .banner--left { left: 190px; }
  .banner--right { left: 678px; }

  .photo { position: absolute; left: 14px; width: 304px; }
  .photo--panel { top: 13px; height: 795px;
    background: linear-gradient(160deg, #eef0ef 0%, #e2e3e2 45%, #d8d5d3 70%, #e9e9e8 100%); }
  .photo--equipment { top: 166px; height: 379px;
    background: linear-gradient(180deg, #c9c9c9 0%, #b7a9a8 60%, #eeeeee 100%); }

  .brand { position: absolute; top: 38px; left: 49px; display: flex; align-items: center; gap: 8px; }
  .brand__mark { width: 98px; height: 98px; border-radius: 50%; background: var(--red); flex: none; }
  .brand__name { color: var(--logo-grey); font-weight: 600; font-size: 26px; line-height: 1.05; text-transform: uppercase; letter-spacing: 0.5px; }

  .hero { position: absolute; left: 14px; top: 166px; width: 304px; height: 364px; color: var(--white); text-align: center; }
  .hero--red { background: var(--red-tint); clip-path: polygon(0 0, 100% 0, 100% 97.5%, 0 100%); }
  .hero--dark { background: var(--charcoal); clip-path: polygon(0 0, 100% 0, 100% 100%, 0 97.5%); }

  .hero__title { position: absolute; top: 28px; left: 1px; width: 280px; font-weight: 800; font-size: 30px; line-height: 37px; letter-spacing: 0.5px; }
  .hero__lede { position: absolute; top: 162px; left: 1px; width: 280px; font-weight: 700; font-size: 8.6px; line-height: 11px; }
  .hero__areas { position: absolute; top: 231px; left: 0; width: 304px; font-weight: 600; font-size: 16.5px; line-height: 20.5px; }

  .services-tag { position: absolute; width: 246px; height: 53px; background: var(--red); color: var(--white);
    font-weight: 800; font-size: 24px; display: flex; align-items: center; justify-content: center; }
  .banner--left .services-tag { left: 42px; top: 573px; }
  .banner--right .services-tag { left: 41px; top: 578px; }

  .services { position: absolute; left: 4px; width: 331px; list-style: none; text-align: center; color: var(--ink); font-weight: 700; font-size: 20px; }
  .banner--left .services { top: 643px; }
  .banner--left .services li { height: 42px; line-height: 28px; }
  .banner--right .services { top: 650px; }
  .banner--right .services li { height: 35px; line-height: 28px; }

  .footer-shape { position: absolute; left: 0; top: 0; width: 331px; height: 992px; }

  .contact { position: absolute; left: 0; top: 870px; width: 331px; text-align: center; color: var(--white); }
  .contact__phone { font-weight: 800; font-size: 31px; line-height: 40px; letter-spacing: 1px; }
  .contact__email { font-weight: 700; font-size: 14px; line-height: 18px; }
  .contact__address { font-weight: 400; font-size: 13px; line-height: 18px; }
</style>
</head>
<body>

<section class="banner banner--left">
  <div class="photo photo--panel" role="img" aria-label="Photo of a hand pressing a red fire alarm unit on a light wall"></div>
  <div class="brand">
    <span class="brand__mark"></span>
    <span class="brand__name">Brightline<br>Works</span>
  </div>
  <div class="hero hero--red">
    <h1 class="hero__title">COMMERCIAL PROPERTY PROTECTION</h1>
    <p class="hero__lede">Brightline Works is your comprehensive<br>Fire Alarm, Security &amp; Electrical Solution Provider.</p>
    <p class="hero__areas">SERVING AUBURN, KENT<br>RENTON, SEATTLE, BELLEVUE<br>LYNNWOOD, MAPLE VALLEY<br>COVINGTON, PUYALLUP.</p>
  </div>
  <div class="services-tag">OUR SERVICES</div>
  <ul class="services">
    <li>FIRE PROTECTION</li>
    <li>SECURITY</li>
    <li>SURVEILLANCE</li>
    <li>ELECTRICAL SERVICES</li>
  </ul>
  <svg class="footer-shape" viewBox="0 0 331 992" aria-hidden="true">
    <polygon points="0,846 331,806 331,992 0,992" fill="var(--red-deep)"/>
    <polygon points="0,855 331,817 331,992 0,992" fill="var(--red)"/>
  </svg>
  <div class="contact">
    <p class="contact__phone">555-014-2290</p>
    <p class="contact__email">office@bwk-qtr.com</p>
    <p class="contact__address">880 Harbor Ridge Rd SE STE 210<br>Auburn, WA 98000</p>
  </div>
</section>

<section class="banner banner--right">
  <div class="photo photo--equipment" role="img" aria-label="Photo of a fire extinguisher and alarm control panel"></div>
  <div class="brand">
    <span class="brand__mark"></span>
    <span class="brand__name">Brightline<br>Works</span>
  </div>
  <div class="hero hero--dark">
    <h1 class="hero__title">COMMERCIAL PROPERTY PROTECTION</h1>
    <p class="hero__lede">Brightline Works is your comprehensive<br>Fire Alarm, Security &amp; Electrical Solution Provider.</p>
    <p class="hero__areas">SERVING AUBURN, KENT<br>RENTON, SEATTLE, BELLEVUE<br>LYNNWOOD, MAPLE VALLEY<br>COVINGTON, PUYALLUP.</p>
  </div>
  <div class="services-tag">OUR SERVICES</div>
  <ul class="services">
    <li>FIRE PROTECTION</li>
    <li>SECURITY</li>
    <li>SURVEILLANCE</li>
    <li>ELECTRICAL SERVICES</li>
  </ul>
  <svg class="footer-shape" viewBox="0 0 331 992" aria-hidden="true">
    <polygon points="0,806 331,846 331,992 0,992" fill="var(--red-deep)"/>
    <polygon points="0,817 331,855 331,992 0,992" fill="var(--red)"/>
  </svg>
  <div class="contact">
    <p class="contact__phone">555-014-2290</p>
    <p class="contact__email">office@bwk-qtr.com</p>
    <p class="contact__address">880 Harbor Ridge Rd SE STE 210<br>Auburn, WA 98000</p>
  </div>
</section>

</body>
</html>
```